Postcard Design for Marketing to Builders

I am an architect that gets most of my work from contractor's. I design residential and commercial projects based in California. My main focus is California's Central Coast. I want the feel of the postcard to reflect a strong professional, efficient and creative partner for contractors (Builders). I have provide some photos of projects I have done recently to use on the postcard if needed. I have also included my logo which I would like on the front.

Industry/Entity Type

Architect

Font styles to use
Serif

```html
<!DOCTYPE html>
<html lang="en">
<head>
<meta charset="utf-8">
<title>Daniel R. Hale – Architect Postcard</title>
<link href="https://fonts.googleapis.com/css2?family=Roboto:wght@300;400;500;700&display=swap" rel="stylesheet">
<style>
  :root {
    --page: #ecebe8;
    --card: #ffffff;
    --orange: #ee6a3c;
    --blue: #4c68c6;
    --navy: #3a3a98;
    --ink-purple: #4b3f9e;
    --white: #ffffff;
    --sky: #8cbbe6;
    --cream: #ece3c2;
    --lawn: #6d9a48;
  }
  * { box-sizing: border-box; margin: 0; padding: 0; }
  html, body { width: 1200px; height: 1000px; overflow: hidden; }
  body {
    background: var(--page);
    font-family: "Roboto", Arial, sans-serif;
    position: relative;
  }
  .postcard {
    position: absolute;
    left: 270px;
    width: 660px;
    height: 440px;
    background: var(--card);
    overflow: hidden;
    box-shadow: 0 4px 14px rgba(0,0,0,0.18);
  }
  .postcard--front { top: 40px; }
  .postcard--back { top: 520px; }
  .postcard__shapes { position: absolute; inset: 0; width: 100%; height: 100%; }

  .brand-name {
    position: absolute;
    font-weight: 500;
    font-size: 12px;
    letter-spacing: 0.04em;
    text-transform: uppercase;
    line-height: 1.2;
  }
  .postcard--front .brand-name { left: 34px; top: 112px; color: var(--navy); }
  .postcard--back .brand-name { right: 30px; bottom: 40px; color: var(--white); text-align: right; }

  .front__headline {
    position: absolute;
    right: 30px;
    top: 222px;
    text-align: right;
    color: var(--white);
    font-size: 22px;
    font-weight: 400;
    line-height: 1.2;
    white-space: nowrap;
  }
  .front__name {
    position: absolute;
    left: 36px;
    top: 298px;
    color: var(--white);
    font-size: 25px;
    font-weight: 500;
  }
  .front__tagline {
    position: absolute;
    left: 36px;
    top: 330px;
    color: var(--ink-purple);
    font-size: 19px;
    font-weight: 400;
    line-height: 1.2;
  }
  .front__contact {
    position: absolute;
    right: 26px;
    top: 326px;
    color: var(--white);
    font-size: 12px;
    font-weight: 300;
    text-align: right;
    line-height: 1.55;
    white-space: nowrap;
  }

  .back__letter {
    position: absolute;
    left: 350px;
    top: 52px;
    width: 272px;
    color: var(--white);
    font-size: 11.5px;
    font-weight: 300;
    line-height: 1.45;
    text-align: justify;
  }
  .back__letter p + p { margin-top: 12px; }
  .back__letter .lorem { text-align: center; text-align-last: center; }
</style>
</head>
<body>

<section class="postcard postcard--front">
  <svg class="postcard__shapes" viewBox="0 0 660 440" xmlns="http://www.w3.org/2000/svg">
    <defs>
      <linearGradient id="frontPhoto" x1="0" y1="0" x2="0" y2="1">
        <stop offset="0" stop-color="var(--sky)"/>
        <stop offset="0.35" stop-color="#b9d2ec"/>
        <stop offset="0.55" stop-color="var(--cream)"/>
        <stop offset="0.85" stop-color="var(--lawn)"/>
        <stop offset="1" stop-color="#8a9a74"/>
      </linearGradient>
    </defs>
    <polygon points="320,0 660,0 660,46" fill="var(--navy)"/>
    <polygon points="300,0 660,12 660,30" fill="var(--blue)"/>
    <g role="img" aria-label="Photo of a single-storey commercial building with gabled glass entrance, landscaped lawn and flower beds">
      <polygon points="0,100 660,40 660,235 0,255" fill="url(#frontPhoto)"/>
    </g>
    <polygon points="0,255 660,235 660,440 0,440" fill="var(--blue)"/>
    <polygon points="0,195 72,276 660,258 660,250" fill="var(--navy)"/>
    <polygon points="0,150 0,178 88,270" fill="var(--orange)"/>
    <polygon points="60,262 660,300 660,205 340,238" fill="var(--orange)"/>
    <polygon points="660,300 660,312 470,292" fill="var(--white)"/>
    <polygon points="0,432 660,372 660,382 0,440" fill="var(--white)"/>
    <polygon points="0,440 660,382 660,440" fill="var(--navy)"/>
  </svg>

  <div class="brand-name">Daniel R Hale<br>Architect</div>
  <h1 class="front__headline">Looking for a residential<br>and commercial Architect?</h1>
  <p class="front__name">Daniel R. Hale</p>
  <p class="front__tagline">Your Professional,<br>Efficient, Creative partner.</p>
  <p class="front__contact">Address: PO Box 2210, Arroyo Vista, CA 93999<br>Phone: (555) 014-2876</p>
</section>

<section class="postcard postcard--back">
  <svg class="postcard__shapes" viewBox="0 0 660 440" xmlns="http://www.w3.org/2000/svg">
    <defs>
      <linearGradient id="housePhoto" x1="0" y1="0" x2="0" y2="1">
        <stop offset="0" stop-color="#9cc6e8"/>
        <stop offset="0.3" stop-color="#c9a08a"/>
        <stop offset="0.7" stop-color="#cdb9a0"/>
        <stop offset="1" stop-color="#8a8a80"/>
      </linearGradient>
      <linearGradient id="smallPhotoA" x1="0" y1="0" x2="0" y2="1">
        <stop offset="0" stop-color="#a9c9e2"/>
        <stop offset="1" stop-color="#6f8a66"/>
      </linearGradient>
      <linearGradient id="smallPhotoB" x1="0" y1="0" x2="0" y2="1">
        <stop offset="0" stop-color="#7fb0e0"/>
        <stop offset="0.6" stop-color="#c8b48e"/>
        <stop offset="1" stop-color="#8a9070"/>
      </linearGradient>
    </defs>
    <polygon points="380,0 660,0 660,40" fill="var(--navy)"/>
    <polygon points="0,290 660,210 660,440 0,440" fill="var(--blue)"/>
    <polygon points="0,415 660,300 660,318 0,432" fill="var(--white)"/>
    <polygon points="0,432 660,318 660,440 0,440" fill="var(--navy)"/>
    <g role="img" aria-label="Photo of a two-storey stucco family home with tiled roof, garage and car in the driveway">
      <polygon points="20,78 330,54 330,262 20,292" fill="url(#housePhoto)"/>
    </g>
    <polygon points="330,28 640,10 640,290 360,300 230,262 330,262" fill="var(--orange)"/>
    <g role="img" aria-label="Photo of a raised beach house with wooden stairs">
      <polygon points="30,320 190,306 190,388 30,404" fill="url(#smallPhotoA)"/>
    </g>
    <g role="img" aria-label="Photo of a multi-storey commercial office building">
      <polygon points="205,304 370,290 370,370 205,386" fill="url(#smallPhotoB)"/>
    </g>
  </svg>

  <div class="back__letter">
    <p>Hello,<br>my name is Daniel R. Hale. I'm an established contractor architect in California's Central Coast and I design residential and commercial projects based in California.</p>
    <p class="lorem">Lorem ipsum dolor sit amet, consectetur adipiscing elit, sed do eiusmod tempor incididunt ut labore et dolore magna aliqua. Ut enim ad minim veniam, quis nostrud exercitation ullamco laboris nisi ut aliquip ex ea commodo consequat. Duis aute irure dolor in reprehenderit in voluptate velit esse cillum dolore eu fugiat nulla pariatur.</p>
  </div>
  <div class="brand-name">Daniel R Hale<br>Architect</div>
</section>

</body>
</html>
```